Business Card Lionel/Marta

We would like you to design a business card with the same graphics as the rack card, which is attached, along with our logo. We are looking for a business card for our company director Lionel Parfitt and for myself (Marta de Wintersloot, General Manager).

Reason: We did not provide all relevant information before the end of the original deadline. The brief has now been updated and the deadline extended.

Industry/Entity Type

Business

Requirements
Must have
• We need the logo and the following contact details:

Lionel Parfitt
Company Director
17 Brindle Lane
Mangere, Auckland, 2022
E: lionel@harbourlink4.co.nz
W: www.harbourlink4.co.nz
P: +64 (0)9 4831907
F: +64 (0)9 4831905
M: +64 (0)21 618447
FREE: 0508 391460 (NZ only)

Marta de Wintersloot
General Manager
17 Brindle Lane
Mangere, Auckland, 2022
E: marta@harbourlink4.co.nz
W: www.harbourlink4.co.nz
P: +64 (0)9 4831907
F: +64 (0)9 4831905
M: +64 (0)21 618448

The phrase "Service Excellence".
Nice to have
• We would like to incorporate icons to indicate "phone", "website", "mobile" etc.

```html
<!DOCTYPE html>
<html lang="en">
<head>
<meta charset="utf-8">
<title>Business Card Lionel/Marta</title>
<link href="https://fonts.googleapis.com/css2?family=Poppins:wght@300;400;500;600;700&display=swap" rel="stylesheet">
<style>
  :root {
    --stage: #5b5b5b;
    --label: #3a3a3a;
    --blue: #1d3c93;
    --red: #e8193a;
    --red-deep: #d0202f;
    --white: #ffffff;
    --silver: #cfcfcf;
  }
  * { margin: 0; padding: 0; box-sizing: border-box; }
  html, body { width: 1200px; height: 1000px; overflow: hidden; }
  body {
    background: var(--stage);
    font-family: "Poppins", sans-serif;
    position: relative;
  }
  .card {
    position: absolute;
    width: 555px;
    height: 342px;
    overflow: hidden;
    background: var(--blue);
    box-shadow: 0 1px 3px rgba(0,0,0,.35);
  }
  .card--lionel { left: 30px; top: 53px; }
  .card--marta { left: 622px; top: 53px; }
  .card--back { left: 622px; top: 515px; background: var(--white); }
  .card__waves { position: absolute; left: 0; top: 0; }
  .card__name {
    position: absolute; left: 0; right: 0; top: 27px;
    text-align: center; color: var(--red);
    font-size: 25px; font-weight: 500; line-height: 1;
  }
  .card__role {
    position: absolute; left: 0; right: 0; top: 57px;
    text-align: center; color: var(--blue);
    font-size: 14px; font-weight: 400; line-height: 1;
  }
  .brand {
    position: absolute; left: 58px; top: 172px; width: 160px;
    color: var(--white); font-weight: 700; line-height: 1;
    text-align: center;
  }
  .brand__name { font-size: 21px; letter-spacing: 0; }
  .brand__sub { font-size: 21px; margin-top: 62px; }
  .divider {
    position: absolute; left: 278px; top: 158px;
    width: 1px; height: 134px; background: rgba(255,255,255,.8);
  }
  .contact {
    position: absolute; left: 290px; top: 157px;
    list-style: none; color: var(--white);
  }
  .contact li {
    display: flex; align-items: center;
    font-size: 15px; font-weight: 300; line-height: 21px; letter-spacing: .2px;
  }
  .contact li.small { font-size: 13.5px; }
  .contact svg { width: 11px; height: 11px; margin-right: 13px; flex: none; }
  .contact .address { align-items: flex-start; line-height: 16px; margin-top: 3px; }
  .contact .address svg { margin-top: 3px; }
  .tollfree {
    position: absolute; left: 0; right: 0; bottom: 0; height: 35px;
    background: var(--red); color: var(--white);
    display: flex; align-items: center; justify-content: center;
    font-size: 15px; font-weight: 600;
  }
  .brand--back {
    position: absolute; left: 0; right: 0; top: 62px;
    text-align: center; color: var(--blue); font-weight: 700; line-height: 1;
  }
  .brand--back .brand__name { font-size: 44px; }
  .brand--back .brand__sub {
    display: inline-block; margin-top: 100px; font-size: 42px;
  }
  .label {
    position: absolute; color: var(--label);
    font-size: 38px; font-weight: 400; line-height: 1;
  }
  .label--lionel { left: 236px; top: 412px; }
  .label--marta { left: 880px; top: 412px; }
  .label--back { left: 877px; top: 880px; }
</style>
</head>
<body>

<svg width="0" height="0" style="position:absolute" aria-hidden="true">
  <defs>
    <linearGradient id="topSheen" x1="0" y1="0" x2="1" y2="0">
      <stop offset="0" stop-color="#bdbdbd"/>
      <stop offset=".5" stop-color="#ffffff"/>
      <stop offset="1" stop-color="#bdbdbd"/>
    </linearGradient>
    <linearGradient id="redBand" x1="0" y1="0" x2="0" y2="1">
      <stop offset="0" stop-color="#e22a36"/>
      <stop offset="1" stop-color="#c81d2b"/>
    </linearGradient>
    <filter id="curveShadow" x="-5%" y="-20%" width="110%" height="150%">
      <feDropShadow dx="0" dy="3" stdDeviation="3" flood-color="#000" flood-opacity=".45"/>
    </filter>
    <symbol id="waves" viewBox="0 0 555 342">
      <path d="M0,0 H555 V62 Q277.5,182 0,62 Z" fill="url(#redBand)" filter="url(#curveShadow)"/>
      <path d="M0,0 H555 V22 Q277.5,132 0,22 Z" fill="url(#topSheen)" filter="url(#curveShadow)"/>
    </symbol>
    <symbol id="i-mobile" viewBox="0 0 11 11"><rect x="0" y="0" width="11" height="11" rx="2" fill="#fff"/><rect x="3.5" y="2" width="4" height="7" rx=".8" fill="none" stroke="#1d3c93" stroke-width="1.1"/></symbol>
    <symbol id="i-phone" viewBox="0 0 11 11"><rect x="0" y="0" width="11" height="11" rx="2" fill="#fff"/><path d="M3,2.5 L4.5,2.5 L5,4.2 L4.2,5 Q5,6.6 6.2,7 L7,6.2 L8.6,6.8 L8.6,8.3 Q5.5,8.8 3.4,6 Q2.4,4.5 3,2.5Z" fill="#1d3c93"/></symbol>
    <symbol id="i-fax" viewBox="0 0 11 11"><rect x="0" y="0" width="11" height="11" rx="2" fill="#fff"/><rect x="2.5" y="5" width="6" height="3.5" fill="#1d3c93"/><rect x="3.5" y="2.5" width="4" height="2.5" fill="none" stroke="#1d3c93" stroke-width="1"/></symbol>
    <symbol id="i-mail" viewBox="0 0 11 11"><rect x="0" y="0" width="11" height="11" rx="2" fill="#fff"/><rect x="2.2" y="3.2" width="6.6" height="4.6" fill="none" stroke="#1d3c93" stroke-width="1"/><path d="M2.2,3.2 L5.5,6 L8.8,3.2" fill="none" stroke="#1d3c93" stroke-width="1"/></symbol>
    <symbol id="i-web" viewBox="0 0 11 11"><circle cx="5.5" cy="5.5" r="5.5" fill="#fff"/><circle cx="5.5" cy="5.5" r="3.3" fill="none" stroke="#1d3c93" stroke-width=".9"/><path d="M2.2,5.5 H8.8 M5.5,2.2 V8.8" stroke="#1d3c93" stroke-width=".9"/></symbol>
    <symbol id="i-pin" viewBox="0 0 11 11"><rect x="0" y="0" width="11" height="11" rx="2" fill="#fff"/><path d="M5.5,9 L3.2,5.4 A2.6,2.6 0 1 1 7.8,5.4 Z" fill="#1d3c93"/><circle cx="5.5" cy="4.2" r="1" fill="#fff"/></symbol>
  </defs>
</svg>

<section class="card card--lionel" aria-label="Business card front, Lionel Parfitt">
  <svg class="card__waves" width="555" height="342" aria-hidden="true"><use href="#waves"/></svg>
  <h2 class="card__name">Lionel Parfitt</h2>
  <p class="card__role">Company Director</p>
  <div class="brand">
    <div class="brand__name">HARBOURLINK4</div>
    <div class="brand__sub">RENTAL CARS</div>
  </div>
  <div class="divider"></div>
  <ul class="contact">
    <li><svg><use href="#i-mobile"/></svg>+64 (0)21 618447</li>
    <li><svg><use href="#i-phone"/></svg>+64 (0)9 4831907</li>
    <li><svg><use href="#i-fax"/></svg>+64 (0)9 4831905</li>
    <li class="small"><svg><use href="#i-mail"/></svg>lionel@harbourlink4.co.nz</li>
    <li class="small"><svg><use href="#i-web"/></svg>www.harbourlink4.co.nz</li>
    <li class="address"><svg><use href="#i-pin"/></svg><span>17 Brindle Lane, Mangere<br>Auckland, 2022</span></li>
  </ul>
  <div class="tollfree">TOLL FREE: 0508 391460 (NZ only)</div>
</section>

<section class="card card--marta" aria-label="Business card front, Marta de Wintersloot">
  <svg class="card__waves" width="555" height="342" aria-hidden="true"><use href="#waves"/></svg>
  <h2 class="card__name">Marta de Wintersloot</h2>
  <p class="card__role">General Manager</p>
  <div class="brand">
    <div class="brand__name">HARBOURLINK4</div>
    <div class="brand__sub">RENTAL CARS</div>
  </div>
  <div class="divider"></div>
  <ul class="contact">
    <li><svg><use href="#i-mobile"/></svg>+64 (0)21 618448</li>
    <li><svg><use href="#i-phone"/></svg>+64 (0)9 4831907</li>
    <li><svg><use href="#i-fax"/></svg>+64 (0)9 4831905</li>
    <li class="small"><svg><use href="#i-mail"/></svg>lionel@harbourlink4.co.nz</li>
    <li class="small"><svg><use href="#i-web"/></svg>www.harbourlink4.co.nz</li>
    <li class="address"><svg><use href="#i-pin"/></svg><span>17 Brindle Lane, Mangere<br>Auckland, 2022</span></li>
  </ul>
  <div class="tollfree">TOLL FREE: 0508 391460 (NZ only)</div>
</section>

<section class="card card--back" aria-label="Business card back">
  <div class="brand--back">
    <div class="brand__name">HARBOURLINK4</div>
    <div class="brand__sub">RENTAL CARS</div>
  </div>
</section>

<p class="label label--lionel">Front</p>
<p class="label label--marta">Front</p>
<p class="label label--back">Back</p>

</body>
</html>
```